Banner ads for do-it-yourself website maker

We need banner ads for a FREE do-it-yourself website maker.

Our website is: http://www.brimlake.com

We are seeking TEN different 720x90 banner ads that convince people to try the product.

The ads should be simple single-image jpgs, although they also could be animated GIFs if the size can be kept down (under 150k)

To see what we offer, check out the website - or, a quick summary follows:

- Free, No need to give credit card, etc
- Do it yourself website builder
- All inclusive (hosting, cloud-based tools)
- One-time fee if want to add your own URL
- Mobile website support
- Easy to use, but powerful enough for PROS
- Websites, or powerful blogging
- Blogging features (blog by email, or via webpage), rss feeds, social media integration
- Full SEO support
- Low-cost option to pay if you want to skill the ads
- Widget-based system (Photo galleries, blog, comment, store, ecommerce, subscription payments, message boards, contact forms)
- Powerful newsletter feature
- Security (integrated user management, lock down the whole site, or individual pages)
Updates

I notice that the first design that came in was five "spins" on one creative idea. At the other end of this process my goal is to come out with ten completely different banners, NOT one idea in ten different designs.

The design that was submitted was excellent and had some great ideas in it.. so, the process does seem to be working. I'm very curious to see everyone's good ideas!

-Dale R

I should also mention...

The ads will be cycled through (on different days/times) when run - so, no one ad has to tell the whole story. My thought is that each ad tells a part of the story (the ads do have to work on their own), but that when combined, with the target audience seeing them over a period of weeks, they get the full message of why our product is great.

Target Market(s)

Our target audience are serious bloggers seeking to make money on their blog. Also small business people (photographers, plumbers, accountants, web designers).

Industry/Entity Type

Credit Card

Colors

Designer to choose colors to be used in the design.

Requirements
Must have
• Grab the person quickly - something that cuts through the clutter. Examples:

"Need a website?
Your website can be live 15 minutes from now!
FREE - why not try now?"

Or ..

"Serious bloggers need serious power. One of our bloggers just surpassed 200,000 readers. Are you ready for action?"

Or ...

"Tired of waiting on a geek to do your website?
Why wait. We have hundreds of professionally designed templates.
Get started now. Do it yourself. Free."

Or...

??? All ideas appreciated.
Nice to have
• Send a message of simple - but, not so simple that we are competing with the simplistic products - We are do it yourself for people who are willing to invest some effort to create something they won't outgrow. If they are looking for a simple one-page website - that is really just an online yellow-pages listing - we may not be right for them. We are do-it-yourself for people who appreciate power, and are willing to do some work to have a free site.

```html
<!DOCTYPE html>
<html lang="en">
<head>
<meta charset="utf-8">
<title>Brimlake – 720x90 banner</title>
<link href="https://fonts.googleapis.com/css2?family=Roboto+Condensed:wght@700;900&display=swap" rel="stylesheet">
<style>
  :root{
    --page:#ffffff;
    --label-tan:#a08f72;
    --label-orange:#e07b14;
    --sea-deep:#3fa6d8;
    --sea-light:#8fd2ee;
    --tan:#9d8d73;
    --tan-dark:#7f6f57;
    --outline:#ffffff;
    --chart:#ffffff;
  }
  html,body{margin:0;padding:0;}
  body{
    width:1200px;height:1000px;overflow:hidden;position:relative;
    background:var(--page);
    font-family:"Roboto Condensed", "Arial Narrow", sans-serif;
  }
  .size-label{
    position:absolute;margin:0;font-weight:700;letter-spacing:.2px;
  }
  .size-label--actual{left:207px;top:256px;font-size:27px;color:var(--label-tan);}
  .size-label--preview{left:54px;top:478px;font-size:27px;color:var(--label-orange);}
  .banner{
    position:absolute;display:block;
    box-shadow:6px 8px 10px rgba(0,0,0,.28);
  }
  .banner--actual{left:207px;top:298px;width:720px;height:90px;}
  .banner--preview{left:54px;top:528px;width:1027px;height:128px;}
  .defs{position:absolute;width:0;height:0;overflow:hidden;}
  .claim{
    font-family:"Roboto Condensed", "Arial Narrow", sans-serif;
    font-weight:900;fill:url(#tanFill);
    stroke:var(--outline);stroke-width:3.2px;paint-order:stroke;stroke-linejoin:round;
  }
  .brand-name{
    font-family:"Roboto Condensed", "Arial Narrow", sans-serif;
    font-weight:700;fill:var(--outline);
  }
</style>
</head>
<body>

<svg class="defs" aria-hidden="true">
  <defs>
    <linearGradient id="sea" x1="0" y1="0" x2="0" y2="1">
      <stop offset="0" stop-color="#6cc3ea"/>
      <stop offset=".5" stop-color="#4fb2df"/>
      <stop offset="1" stop-color="#8fd2ee"/>
    </linearGradient>
    <linearGradient id="tanFill" x1="0" y1="0" x2="0" y2="1">
      <stop offset="0" stop-color="#7f6f57"/>
      <stop offset="1" stop-color="#b3a58c"/>
    </linearGradient>
    <linearGradient id="dotFill" x1="0" y1="0" x2="0" y2="1">
      <stop offset="0" stop-color="#8a7a60"/>
      <stop offset="1" stop-color="#c2b59d"/>
    </linearGradient>
    <symbol id="bannerArt" viewBox="0 0 720 90">
      <rect class="sea" width="720" height="90" fill="url(#sea)" role="img" aria-label="Blue water surface background"/>

      <g class="growth-chart" fill="none" stroke="var(--chart)" stroke-opacity=".45" stroke-width="3">
        <polyline points="60,62 118,36 160,28 198,58"/>
        <polyline points="520,72 575,30 612,20 640,42 668,6 694,26 720,12"/>
        <g fill="var(--chart)" fill-opacity=".45" stroke="none">
          <circle cx="118" cy="36" r="6"/><circle cx="160" cy="28" r="7"/>
          <circle cx="575" cy="30" r="6"/><circle cx="612" cy="20" r="7"/>
          <circle cx="640" cy="42" r="6"/><circle cx="668" cy="6" r="6"/>
          <circle cx="694" cy="26" r="7"/>
        </g>
      </g>

      <g class="brand">
        <text class="brand-name" x="14" y="45" font-size="14">BRIMLAKE</text>
      </g>

      <text class="claim" x="81" y="44" font-size="15" letter-spacing=".5">SIMPLE</text>
      <circle cx="123" cy="65" r="12" fill="url(#dotFill)" stroke="var(--outline)" stroke-width="1.5"/>
      <text class="claim" x="141" y="71" font-size="20" letter-spacing=".5">EASY</text>

      <g class="template-cards">
        <g transform="rotate(-3 247 47)">
          <rect x="197" y="6" width="100" height="80" rx="4" fill="#fff"/>
          <rect x="201" y="10" width="92" height="72" fill="#d9dde4" role="img" aria-label="Screenshot of a store website template"/>
          <rect x="201" y="10" width="92" height="5" fill="#1f3d73"/>
        </g>
        <rect x="300" y="0" width="122" height="90" fill="#d9c9a8" role="img" aria-label="Screenshot of a parchment style website template"/>
        <g transform="rotate(3 475 46)">
          <rect x="425" y="4" width="100" height="82" rx="4" fill="#fff"/>
          <rect x="429" y="8" width="92" height="74" fill="#b9652e" role="img" aria-label="Screenshot of a restaurant website template"/>
        </g>
      </g>

      <text class="claim" x="240" y="50" font-size="35" textLength="245" lengthAdjust="spacingAndGlyphs">DO IT YOURSELF</text>
      <text class="claim" x="241" y="72" font-size="22" textLength="240" lengthAdjust="spacing">WEBSITE BUILDER</text>

      <text class="claim" x="546" y="58" font-size="22" letter-spacing=".5">FREE</text>
      <circle cx="617" cy="47" r="12" fill="url(#dotFill)" stroke="var(--outline)" stroke-width="1.5"/>
      <text class="claim" x="599" y="79" font-size="14" textLength="100" lengthAdjust="spacingAndGlyphs">PROFESSIONAL</text>
    </symbol>
  </defs>
</svg>

<h2 class="size-label size-label--actual">size 720x90</h2>
<svg class="banner banner--actual" viewBox="0 0 720 90" role="img" aria-label="Brimlake banner: Simple, easy, do it yourself website builder, free, professional">
  <use href="#bannerArt" width="720" height="90"/>
</svg>

<h2 class="size-label size-label--preview">enlarged size for preview</h2>
<svg class="banner banner--preview" viewBox="0 0 720 90" preserveAspectRatio="none" role="img" aria-label="Brimlake banner enlarged">
  <use href="#bannerArt" width="720" height="90"/>
</svg>

</body>
</html>
```